The next stage in our 106 year history in Specialised Stationery

We need a business card design(which is also adaptable for our general stationery) to suit the changing face of our business. Harlow, an Australian company has been the leader in its category since 1907. We design and print various books required by small business to comply with government legislation in regards to keeping records. Accountancy, Payroll, Vehicle usage recording, Firearms registration etc. The Harlow logo a blue diamond is one of the best known in our industry. As manual recording has declined in the last few years we have diversified into other areas: Safety Apparel, Personal Protective Equipment (PPE) and web based software for bookkeeping and Customer Relationship management(CRM). Separate logos have been adopted for each of these being: Harlow Systems, Harlow Safety, Harlow Apparel and Harlow Software each with same diamond but different colour background. This has made it easy to identify the different sectors but difficult to bring together for a Corporate identity in Business cards etc. We are looking to bring all logos together (not one logo) but still allow the logo to depict the diversity of our offering, while still being able to have a category specific logo for each of the divisions. All products go through the same distribution channel, Office Products. The final design should depict an old established company well, known and trusted but leaping forward and still retaining same values they have come to trust.

Target Market(s)

Micro to small business companies generally who employ 20 or less people.

Industry/Entity Type

Small Business

Requirements
Must have
• The diamonds are well recognised and the new design should retain the integrity of them.

```html
<!DOCTYPE html>
<html lang="en">
<head>
<meta charset="utf-8">
<title>Harlow Business Card</title>
<link href="https://fonts.googleapis.com/css2?family=Cinzel:wght@400;600;700&display=swap" rel="stylesheet">
<style>
  :root {
    --backdrop: #4f5656;
    --card-black: #0b0b0b;
    --card-white: #f6f6f4;
    --rule-blue: #1f6fc0;
    --name-blue: #1d5fa8;
    --ink: #2a2a2a;
    --software-red: #c8202f;
    --core-blue: #1f6fc0;
    --apparel-green: #2f9e3c;
    --safety-orange: #e2541c;
    --systems-blue: #1f6fc0;
  }
  * { box-sizing: border-box; margin: 0; padding: 0; }
  html, body {
    width: 1200px; height: 900px; overflow: hidden;
    background: var(--backdrop);
    font-family: "Cinzel", Georgia, serif;
  }
  .canvas {
    width: 1200px; height: 900px;
    display: flex; flex-direction: column; align-items: center; justify-content: center;
    gap: 40px;
  }
  .card {
    position: relative;
    width: 640px; height: 392px;
    background: var(--card-black);
    overflow: hidden;
    box-shadow: 0 14px 30px rgba(0,0,0,.45);
  }

  /* Front */
  .card-front .logo-zone {
    position: absolute; top: 0; left: 0; right: 0; height: 104px;
    display: flex; align-items: center; justify-content: center; gap: 12px;
  }
  .brand-mark { width: 18px; height: 18px; background: var(--core-blue); }
  .brand-name {
    color: var(--core-blue); font-weight: 700; font-size: 38px; letter-spacing: 2px;
  }
  .card-front .info-band {
    position: absolute; top: 104px; left: 0; right: 0; height: 250px;
    background: var(--card-white);
    border-top: 3px solid var(--rule-blue);
    border-bottom: 3px solid var(--rule-blue);
    text-align: center;
  }
  .gem-decoration {
    position: absolute; left: 50%; top: 30px; transform: translateX(-50%);
    width: 220px; height: 150px; border-radius: 40%;
    background: radial-gradient(ellipse at center, rgba(190,196,204,.45), rgba(246,246,244,0) 70%);
  }
  .holder-name {
    position: relative; margin-top: 46px;
    color: var(--name-blue); font-size: 26px; font-weight: 600; letter-spacing: 3px;
  }
  .holder-title {
    position: relative; color: #555; font-size: 15px; letter-spacing: 2px; margin-top: 2px;
  }
  .divider {
    position: relative; width: 70%; height: 1px; margin: 12px auto 14px;
    background: linear-gradient(90deg, transparent, var(--rule-blue), transparent);
  }
  .contact-line {
    position: relative; color: var(--ink); font-size: 13.5px; line-height: 1.65; letter-spacing: .5px;
  }

  /* Back */
  .card-back .division-band {
    position: absolute; top: 138px; left: -80px; width: 800px; height: 116px;
    background: var(--card-white);
    border-top: 3px solid var(--rule-blue);
    border-bottom: 3px solid var(--rule-blue);
    transform: rotate(-12deg);
    transform-origin: center;
    display: grid; grid-template-columns: repeat(5, 1fr); align-items: center;
    padding: 0 50px;
  }
  .division {
    display: flex; align-items: center; justify-content: center; gap: 6px;
    font-weight: 700; font-size: 12px; letter-spacing: .3px; white-space: nowrap;
  }
  .division .swatch { width: 10px; height: 10px; flex: none; }
  .division.software { color: var(--software-red); }
  .division.software .swatch { background: var(--software-red); }
  .division.core { color: var(--core-blue); }
  .division.core .swatch { background: var(--core-blue); }
  .division.apparel { color: var(--apparel-green); }
  .division.apparel .swatch { background: var(--apparel-green); }
  .division.safety { color: var(--safety-orange); }
  .division.safety .swatch { background: var(--safety-orange); }
  .division.systems { color: var(--systems-blue); }
  .division.systems .swatch { background: var(--systems-blue); }
</style>
</head>
<body>
<main class="canvas">
  <section class="card card-front">
    <div class="logo-zone">
      <span class="brand-mark"></span>
      <span class="brand-name">Harlow</span>
    </div>
    <div class="info-band">
      <div class="gem-decoration" role="img" aria-label="Faint cut diamond decoration behind the name"></div>
      <h1 class="holder-name">Adrian Kessler</h1>
      <p class="holder-title">CEO</p>
      <div class="divider"></div>
      <p class="contact-line">Harlow Pty Limited, Unit 4, 72 Carramar Road, Kingsgrove, NSW 2208</p>
      <p class="contact-line">Tel: 61 2 9000 1234 | Fax: 61 2 9000 5678 | Mob: 400-555-010</p>
      <p class="contact-line">Email: info@harlowrecords.com | www.harlowrecords.com.au</p>
    </div>
  </section>

  <section class="card card-back">
    <div class="division-band">
      <span class="division software"><span class="swatch"></span>Harlow Software</span>
      <span class="division core"><span class="swatch"></span>Harlow</span>
      <span class="division apparel"><span class="swatch"></span>Harlow Apparel</span>
      <span class="division safety"><span class="swatch"></span>Harlow Safety</span>
      <span class="division systems"><span class="swatch"></span>Harlow Systems</span>
    </div>
  </section>
</main>
</body>
</html>
```